Harborline Energy - needs a business card

Harborline Energy is a U.S. based diesel sourcing and distribution company that supports American oil & gas fields through providing quality product and consistent services.

Target Market(s)

Oil and Gas

Contact Information for Business Card

The background of the card must be white to ensure the logo pops.

Font styles to use
Serif
Sans Serif

Colors

Designer to choose colors to be used in the design.

Requirements
Must have
• Front of Card: Tag line: Harborline Energy, Powering America's Oil & Gas fields.
• Not sure if you guys do this part but just in case...
• Dale Menschow
• Owner/CEO
• C:555.318.4076
• E:Dmenschow@harborlineenergy.example
• W:Harborlineenergy.example
• Locations: Servicing the Powder River, DJ basin and Bakken formations.
• Back of Card: " Frac fueling is what we do. We understand how important diesel fuel is to your operation, which is why our main service line is Frac fueling. We assure our supply and stand by our service"

```html
<!DOCTYPE html>
<html lang="en">
<head>
<meta charset="utf-8">
<title>Harborline Energy — Business Card</title>
<link rel="stylesheet" href="https://fonts.googleapis.com/css2?family=Open+Sans:ital,wght@0,400;0,600;0,700;1,400&display=swap">
<style>
  :root {
    --navy: #1e3466;
    --red: #c62a33;
    --red-dark: #8e1c23;
    --white: #ffffff;
    --paper: #f6f6f6;
    --ghost: #ececec;
    --stage: #e9e6e1;
  }
  * { box-sizing: border-box; margin: 0; padding: 0; }
  html, body { width: 1200px; height: 942px; overflow: hidden; }
  body {
    background: var(--stage);
    font-family: "Open Sans", sans-serif;
    position: relative;
  }
  .card {
    position: absolute;
    left: 240px;
    width: 720px;
    height: 411px;
    background: linear-gradient(135deg, var(--white), var(--paper));
    box-shadow: 0 6px 18px rgba(0,0,0,.18);
    overflow: hidden;
  }
  .card--front { top: 30px; }
  .card--back { top: 501px; }
  .card-art { position: absolute; inset: 0; }

  .ghost-mark {
    position: absolute;
    border-radius: 50%;
    background: radial-gradient(circle, var(--ghost) 0%, rgba(236,236,236,0) 70%);
  }
  .card--front .ghost-mark { left: 400px; top: 180px; width: 300px; height: 300px; }
  .card--back .ghost-mark { left: -40px; top: 40px; width: 380px; height: 380px; }

  .ribbon-name {
    position: absolute;
    left: 44px; top: 44px;
    color: var(--white);
    font-size: 25px;
    font-weight: 400;
    letter-spacing: 1px;
    text-transform: uppercase;
    white-space: nowrap;
  }
  .role {
    position: absolute;
    left: 44px; top: 100px;
    color: var(--red);
    font-size: 14px;
  }
  .contact-list {
    position: absolute;
    left: 44px; top: 136px;
    list-style: none;
    color: var(--white);
    font-size: 15px;
    line-height: 30px;
  }
  .contact-list li { display: flex; align-items: center; gap: 12px; white-space: nowrap; }
  .contact-list svg { width: 12px; height: 12px; flex: none; }
  .service-area {
    position: absolute;
    left: 44px; top: 300px;
    color: var(--white);
    font-size: 14px;
    font-style: italic;
    line-height: 22px;
    white-space: nowrap;
  }
  .brand {
    position: absolute;
    display: flex; align-items: center; gap: 12px;
    color: var(--navy);
    font-weight: 700;
    font-size: 22px;
    letter-spacing: 1px;
    text-transform: uppercase;
    white-space: nowrap;
  }
  .brand-dot {
    width: 40px; height: 40px;
    border-radius: 50%;
    background: var(--red);
  }
  .card--front .brand { right: 30px; bottom: 60px; }
  .card--back .brand { right: 70px; bottom: 70px; }

  .pitch {
    position: absolute;
    left: 250px; top: 38px;
    width: 420px;
    font-size: 15px;
    line-height: 21px;
  }
  .pitch-title { color: var(--red); font-weight: 400; font-size: 15px; }
  .pitch-rule { width: 50px; height: 1px; background: var(--navy); margin: 10px 0 8px; }
  .pitch-body { color: var(--navy); }
  .pitch-promise { color: var(--red); }
</style>
</head>
<body>

<section class="card card--front" aria-label="Front of business card">
  <div class="ghost-mark" role="img" aria-label="Faint brand emblem watermark"></div>
  <svg class="card-art" viewBox="0 0 720 411" aria-hidden="true">
    <polygon points="0,0 440,0 360,411 0,411" fill="var(--navy)"/>
    <polygon points="0,36 330,36 350,88 0,88" fill="var(--red)"/>
    <polygon points="330,88 350,88 336,98" fill="var(--red-dark)"/>
  </svg>
  <h1 class="ribbon-name">Dale Menschow</h1>
  <p class="role">Owner/CEO</p>
  <ul class="contact-list">
    <li>
      <svg viewBox="0 0 12 12"><rect x="3" y="1" width="6" height="10" rx="1" fill="none" stroke="var(--red)" stroke-width="1.2"/></svg>
      555.318.4076
    </li>
    <li>
      <svg viewBox="0 0 12 12"><rect x="1" y="2.5" width="10" height="7" fill="var(--red)"/><polyline points="1,2.5 6,7 11,2.5" fill="none" stroke="var(--white)" stroke-width="1"/></svg>
      Dmenschow@harborlineenergy.example
    </li>
    <li>
      <svg viewBox="0 0 12 12"><circle cx="6" cy="6" r="5" fill="none" stroke="var(--red)" stroke-width="1.2"/><ellipse cx="6" cy="6" rx="2.2" ry="5" fill="none" stroke="var(--red)" stroke-width="1"/><line x1="1" y1="6" x2="11" y2="6" stroke="var(--red)" stroke-width="1"/></svg>
      Harborlineenergy.example
    </li>
  </ul>
  <p class="service-area">Servicing the<br>Powder River, DJ basin and Bakken formations</p>
  <div class="brand"><span class="brand-dot"></span>Harborline Energy</div>
</section>

<section class="card card--back" aria-label="Back of business card">
  <div class="ghost-mark" role="img" aria-label="Faint brand emblem watermark"></div>
  <div class="pitch">
    <h2 class="pitch-title">Frac fueling is what we do</h2>
    <div class="pitch-rule"></div>
    <p class="pitch-body">We understand how important diesel fuel is to your operation, which is why our main service line is Frac fueling</p>
    <div class="pitch-rule"></div>
    <p class="pitch-promise">We assure our supply and stand by our service</p>
  </div>
  <div class="brand"><span class="brand-dot"></span>Harborline Energy</div>
</section>

</body>
</html>
```